Cruise price comparison web design project

The project's name is Wellenfuchsportal.
www.wellenfuchsportal.de
The current design (which I don't really like) can be found here:
http://wfp02.wellenfuchsportal.de/

I m not too happy with what the current developers have been done so far (in terms of design), so I hope to find a great designer her to develop a design that kicks arses. : )

We are currently developing a site for the German market that brings travel agents and cruise holiday makers together. We are not an ordinary travel agency.
Wellenfuchsportal is a quick and convenient way to have independent travel agencies compete to offer our site visitors the best cruise deal available in Europe.

Here is a short video that explains what one of our competitors does; it gives a good overview as our site will be similar:
http://www.voyabidder.com/video_how_voyabidder_works.php
(Voyabidder.com is not a great website in terms of design, so please dont get me wrong.)

The logo has already been created, but both the colours (should remain blueish) and the font can be modified. The font colour can be changed dramatically if you think this is of advantage.

The Website design should be professional and unique and become an eye catcher. It must attract visitors of all age groups, a "wow-effect" is definitely a bonus.
Users should easily see what this website is about.

We need the following text on our homepage:

"Immer der beste Preis -
denn Reisebüros kämpfen um Sie!"
(means "Always the best rate - as travel agents compete offer the best deal")
This is a sort of headline.

We also need:

So funktioniert Wellenfuchsportal:
1. Wunschkreuzfahrt wählen
2. Angebote erhalten und vergleichen
3. Reisebüro kontaktieren und buchen

(This explains briefly how our system works.)

Aside banners maybe needed later for advertising.

Additions I need on the front page are:
- Login / Sign-Up / Your benefits
(I quite like the way it's done on http://www.lirmatimes.com, at the very top of the page)
- Recommendation-link
(for everything else: Pls. refer to wfp02.wellenfuchsportal.de
- 3 or 4 "top offers of the week"
(current format is not very appealing; offers can be displayed as on http://sailings.tripnuvo.com/affiliate/promo.rvlx?OfferID=DOLUMA27 or

A maritime look is surely an option here, as we focus on cruises. But maybe you can surprise me with a great idea.

I quite like the designs where basically one photo / picture is used.
Some examples which look great IMHO:
http://pell-works.artfolioz.com/art/Glint-Swimmers-519304826
http://quorvanwebdesign.artfolioz.com/art/Website-Design-736152940
The following designer has also done a great job:
http://pixelmaker4387.artfolioz.com/gallery/

ATTACHED:
- logo
- Glint-Swimmers Design .png
- Flyer we use to attract travel agencies
- photo we use for the flyer (we own the rights)

Please get in touch with me if there are any questions or if you require further details. I ll get back to all inquiries / messages as soon as possible, usually within a few hours... Feel free to ask technical questions, too, (if any), the developer will be of assistance.

Reason: I decided to extend the deadline to have more time to comment on your designs and allow you to submit a few more proposals.

Reason: Sorry, more time needed to comment on all designs. Apart from this, some designers asked for more time.

Dear All,

Thank you so much for all your proposals.
Later today I will have a decent internet connection connection again, so I will be able to finally comment on your ideas and visions.

Hopefully next week we can finalize this project. Feel free to submit more designs or ask any questions if there are any.
Remember: Wellenfuchsportal won't be an ordinary travel agent. It brings cruise holiday makers and travel agents together.

Best

Target Market(s)

Holidaymakers / potential cruise holiday makers between 20 and 80.

Industry/Entity Type

Advertising

Requirements
Should not have
• Design should not use old-style, serif fonts.

```html
<!DOCTYPE html>
<html lang="de">
<head>
<meta charset="utf-8">
<title>Wellenfuchsportal – Kreuzfahrt-Schnäppchen</title>
<link rel="stylesheet" href="https://fonts.googleapis.com/css2?family=Arimo:ital,wght@0,400;0,700;1,700&family=Cabin:wght@400;500;600&family=Roboto+Condensed:wght@400;500&family=Tinos&display=swap">
<style>
:root{
  --sky-top:#5d8fc4;
  --sky-low:#c9dcec;
  --hull:#e9eef3;
  --sea-deep:#0c2a5e;
  --sea-mid:#1c4c8c;
  --deck:#6b4128;
  --deck-dark:#3e2414;
  --navy:#0f2a8a;
  --nav-blue:#173f9e;
  --white:#ffffff;
  --link-cyan:#27c3f0;
  --button-text:#0a2fa0;
  --footer-dark:#1b1208;
}
*{box-sizing:border-box;margin:0;padding:0}
html,body{width:1200px;height:900px;overflow:hidden}
body{position:relative;font-family:"Cabin",sans-serif;color:var(--white)}
.backdrop{
  position:absolute;inset:0;
  background:
    linear-gradient(180deg,transparent 0 700px,rgba(107,65,40,.0) 700px),
    linear-gradient(180deg,var(--sky-top) 0,var(--sky-low) 90px,var(--hull) 150px,#dfe7ef 205px,var(--sea-mid) 225px,var(--sea-deep) 420px,#123a78 640px,var(--deck) 700px,var(--deck-dark) 900px);
}
.abs{position:absolute}
.brand{left:26px;top:22px;display:flex;align-items:center;gap:8px}
.brand-dot{width:46px;height:46px;border-radius:50%;background:var(--navy)}
.brand-name{font-family:"Cabin",sans-serif;font-weight:600;font-size:15px;color:var(--navy)}
.site-title{left:0;width:1220px;top:14px;text-align:center;font-family:"Tinos",serif;font-size:50px;letter-spacing:1px;color:var(--navy)}
.tagline{left:0;width:1220px;top:86px;text-align:center;font-family:"Arimo",sans-serif;font-weight:700;font-size:22px;color:var(--nav-blue)}
.hotline{right:12px;top:22px;text-align:right;font-family:"Arimo",sans-serif;font-size:14px}
.hotline strong{display:block;font-weight:400;font-size:17px;margin-top:10px}
.account{right:12px;top:92px;font-family:"Arimo",sans-serif;font-weight:700;font-size:16px;display:flex;gap:22px}
.main-nav{left:60px;top:168px;display:flex;gap:21px;font-family:"Roboto Condensed",sans-serif;font-weight:500;font-size:23px;color:var(--nav-blue)}
.hero-head{left:0;width:1200px;top:232px;text-align:center;font-family:"Arimo",sans-serif;font-weight:700;font-variant:small-caps;font-size:29px;letter-spacing:1px;text-shadow:0 2px 3px #000}
.hero-sub{left:0;width:1200px;top:270px;text-align:center;font-family:"Arimo",sans-serif;font-weight:700;font-size:22px;text-shadow:0 2px 3px #000}
.offer-photo{position:absolute;border:2px solid #b7d9ee;border-radius:8px;box-shadow:0 0 8px #7fc0e8}
.offer-photo span{position:absolute;left:0;right:0;bottom:10px;text-align:center;font-size:14px;text-shadow:0 1px 2px #000}
.photo-a{left:16px;top:348px;width:184px;height:148px;background:linear-gradient(180deg,#9fc3e4,#e6ecf2 55%,#2d5fa3 80%)}
.photo-b{left:414px;top:551px;width:184px;height:146px;background:linear-gradient(180deg,#cfd8dd,#8a8f8a 50%,#7a5a3c)}
.offer{font-family:"Cabin",sans-serif;font-weight:500;text-shadow:0 1px 2px #000}
.offer-a{left:250px;top:330px;width:346px;text-align:right;font-size:15px;line-height:21px}
.offer-a h3{font-size:17px;font-weight:500;margin-bottom:14px}
.offer-a p{margin-bottom:8px}
.price{font-size:15px;line-height:20px;text-align:left}
.btn{background:var(--white);color:var(--button-text);font-family:"Arimo",sans-serif;font-size:15px;padding:2px 6px;box-shadow:3px 3px 3px rgba(0,0,0,.6);text-shadow:none}
.price-a{left:257px;top:461px}
.btn-a{left:448px;top:472px}
.offer-b{left:16px;top:540px;font-size:15px;line-height:20px}
.offer-b h3{font-size:18px;font-weight:500;margin-bottom:14px}
.offer-b p{margin-bottom:12px}
.btn-b{left:152px;top:673px}
.steps{right:12px;top:325px;text-align:right;font-family:"Cabin",sans-serif;font-weight:600;text-shadow:0 1px 2px #000}
.steps h2{font-size:23px;font-weight:600;margin-bottom:40px}
.steps li{list-style:none;font-size:16px;margin-bottom:12px}
.signup-note{right:12px;top:584px;text-align:right;font-family:"Arimo",sans-serif;font-size:16px;line-height:20px}
.signup-note b{color:var(--link-cyan)}
.footer-links{top:745px;font-family:"Arimo",sans-serif;font-size:13px;line-height:17px}
.footer-links li{list-style:none}
.col1{left:16px}.col2{left:305px}.col3{left:777px}.col4{left:952px}
.footer-text{left:18px;top:838px;width:1168px;font-family:"Arimo",sans-serif;font-size:11.5px;line-height:13px;color:var(--footer-dark)}
.copyright{right:14px;top:864px;font-family:"Arimo",sans-serif;font-size:11.5px;color:var(--footer-dark)}
</style>
</head>
<body>
<div class="backdrop" role="img" aria-label="Foto: Kreuzfahrtschiff am Himmel oben, tiefblaues Meer und Blick über den Bug mit Holzdeck"></div>

<div class="abs brand"><span class="brand-dot"></span><span class="brand-name">Wellenfuchsportal</span></div>
<h1 class="abs site-title">WELLENFUCHSPORTAL</h1>
<p class="abs tagline">Immer Der Beste Preis - Denn Reise Buros Kampfen Um Sie!</p>
<div class="abs hotline">Mit Kreuzfahrt-Experten Sprechen<strong>02871-539264</strong></div>
<div class="abs account"><span>Log In</span><span>Sign Up</span></div>

<nav class="abs main-nav"><span>So Gehts</span><span>Angebote Erhalten</span><span>Kreuzfahrtsuche</span><span>Reedereien Und Schiffe</span><span>Specials</span><span>Kontakt</span><span>Fehlermeldung</span><span>Trac</span></nav>

<h2 class="abs hero-head">Finden Sie Ihr Kreuzfahrt - Scnappchen!</h2>
<p class="abs hero-sub">Hier finden Sie wochenaktuell eine Auswahl der attraktivsten Kreuzfahrt - Angebote</p>

<div class="offer-photo photo-a" role="img" aria-label="Foto des Kreuzfahrtschiffs auf See"><span>Grace of the Waves</span></div>
<div class="abs offer offer-a">
  <h3>Von der Stadt des Tangos zum Big Apple</h3>
  <p>Inkl. Flugen mit Aerovia, Transfers &amp;<br>Hotelubernachtung in Buenos Aires</p>
  <p>22 Tage Sudamerika Kreuzfahrt<br>Termin&nbsp; Juli 2012</p>
</div>
<div class="abs offer price price-a">ab Euro&nbsp; 2.899<br>Pro Person</div>
<span class="abs btn btn-a">Angebot Bestellen</span>

<div class="abs offer offer-b">
  <h3>Rund um Island - ab/bis Hamburg</h3>
  <p>Top - Angebot</p>
  <p>12 Tage Island Kreuzfahrt<br>Termin&nbsp; 26. Juni 2012</p>
  <p style="margin-top:16px">ab Euro 1.300<br>Pro Person</p>
</div>
<span class="abs btn btn-b">Angebot Bestellen</span>
<div class="offer-photo photo-b" role="img" aria-label="Foto eines Schiffsdecks mit Holzplanken und Reling"><span>Aurora of the Waves</span></div>

<div class="abs steps">
  <h2>So Funktioniert Wellenfuchsportal:</h2>
  <ol><li>1. Wunschkreuzfahrt Wahlen</li><li>2. Angebote Erhalten Und Vergleichen</li><li>3. Reiseburo Kontaktieren Und Buchen</li></ol>
</div>
<p class="abs signup-note">Angebote und Gesuche<br>Kostenlos einstellen - jetzt<br><b>anmelden</b> oder neu <b>registrieren</b></p>

<ul class="abs footer-links col1"><li>Uber uns</li><li>Uber Wellenfuchsportal.de</li><li>Jobs</li><li>Partner</li><li>Werbung auf Wellenfuchsportal.de</li></ul>
<ul class="abs footer-links col2"><li>Presse</li><li>Pressematerial</li><li>Wellenfuchsportal.de in den Medien</li><li>Pressemitteilungen</li><li>Wellenfuchsportal und die Sozialen Medien</li></ul>
<ul class="abs footer-links col3"><li>Hilfe &amp; Service</li><li>Kundenmeinungen</li><li>Kontakt</li><li>FAQ's</li></ul>
<ul class="abs footer-links col4"><li>Rechtiches</li><li>Disclaimer / Haftungsausschluss</li><li>Nutzungsbedingungen</li><li>Impressum</li></ul>

<p class="abs footer-text">Wellenfuchsportal.de ist ein völlig neuer Service, welcher Sie schnell und bequem den günstigsten Preis für eine Kreuzfahrt finden lässt. Lange Suchen nach preiswerten Kreuzfahrten gehören ab sofort der Vergangenheit an, denn Reisebüros kämpfen um Sie. Sparen Sie bares Geld und testen Sie Wellenfuchsportal.de - natürlich völlig kostenlos. Finden Sie Ihr Kreuzfahrt - Schnäppchen!<br>Zuletzt aktualisiert: 05.12.2012</p>
<p class="abs copyright">C 2010-2012 Wellenfuchsportal.de</p>
</body>
</html>
```